Marisol Penhaw tutoring Advertising package - flyers, posters, business card and logo

I am looking for a flyer design for my tutoring business, it needs to explain what tutoring services I offer, how much I charge, why my services are worthwhile, it should include some photos of me and the tutoring centre,

It needs to include my phone number and my website. It should quote from some of the testimonials I have received from parents and children.

My website is www.marisolpenhaw.example My Facebook page can be found at https://www.facebook.example/marisolpenhawtutoring These pages include a range of photos and quotes that you can use.

I am not sure about the colours and designs that I would like, that's why I'm using Artflock!
I'm looking to appeal to parents inform them of my skills and experience.

I'm charging $45 for sessions of an hour and 15 minutes. 2 sessions per week will cost $80. I tutor Monday to Friday afternoons and evenings along with all day Saturdays. The assessment is free.

I tutor children from K-9 in English and Maths. I'm mainly aiming at parents whose children are struggling a little bit at school although I can help children who are doing well too.
I am highly skilled at helping children who can't read, I have a comprehensive program, the Calder program, that specifically teaches children the skills they need to read fluently and successfully.

Similarly I have had a lot of experience at helping children improve their Maths skills. I am well resourced with a wide range of hands on resources, paper resources and electronic resources.

Children will get better NAPLAN results if I tutor them (NAPLAN is the national series of tests in Australia).

I'm after a DL double sided flyer, and an A4 flyer. I'm also looking for two A2 posters and two A3 posters. Finally, I want a business card too. I don't have a logo for the business and I'd love to have one!

Target Market(s)

Parents of school aged children

Industry/Entity Type

Education

Colors

Designer to choose colors to be used in the design.

Requirements
Must have
• my name, my photo, length and cost of my sessions, email and phone contact details. Subjects and age ranges that I teach, times that I tutor. Website and/or Facebook page references. Quotes from Testimonials
Nice to have
• The A2 and A3 posters should complement each other.

```html
<!DOCTYPE html>
<html lang="en">
<head>
<meta charset="utf-8">
<title>Marisol Penhaw Tutoring – A4 Flyer</title>
<link href="https://fonts.googleapis.com/css2?family=Lato:ital,wght@0,400;0,700;0,900;1,700&display=swap" rel="stylesheet">
<style>
  :root{
    --bg:#e6ebed;
    --teal-deep:#0e3a3e;
    --teal-dark:#13484d;
    --teal:#1b7482;
    --teal-bright:#2a9eae;
    --teal-pale:#cfe8ec;
    --ink-dark:#1a1c1e;
    --ink-mid:#3b3e41;
    --white:#ffffff;
    --tag:#2a2e32;
  }
  *{box-sizing:border-box;margin:0;padding:0}
  html,body{width:1200px;height:848px;overflow:hidden}
  body{background:var(--bg);font-family:"Lato",sans-serif;display:flex;justify-content:center;align-items:center}
  .flyer{position:relative;width:600px;height:848px;background:var(--white);overflow:hidden;box-shadow:0 4px 18px rgba(0,0,0,.18)}
  .flyer__topline{position:absolute;top:0;left:0;right:0;height:8px;background:var(--teal-deep);z-index:3}
  .centre-photo{position:absolute;top:8px;left:0;right:0;height:290px;
    background:linear-gradient(160deg,#d9d2c4 0%,#c9b9a0 30%,#b06a34 55%,#8c4f2a 70%,#c58a4a 100%)}
  .headline-band{position:absolute;top:256px;left:0;width:600px;height:140px;z-index:2}
  .headline{position:absolute;top:278px;left:30px;right:30px;z-index:3;color:var(--white);
    font-weight:900;font-size:19.5px;line-height:1.28;text-align:center}
  .about{position:absolute;top:386px;left:0;right:0;height:290px;
    background:linear-gradient(180deg,var(--white) 0%,#eef7f8 45%,var(--teal-pale) 100%)}
  .about__text{position:absolute;top:20px;left:30px;width:345px;color:var(--teal);font-size:10.8px;line-height:1.33;font-weight:700}
  .about__text p{margin-bottom:8px}
  .tutor{position:absolute;top:402px;right:26px;width:188px;z-index:4}
  .tutor__photo{width:188px;height:166px;border:5px solid var(--teal-bright);border-radius:16px;
    background:linear-gradient(170deg,#d8dcd6 0%,#b9c6b0 45%,#7fae57 80%,#6a9b45 100%)}
  .tutor__name{position:relative;margin:-18px auto 0;width:166px;padding:9px 0;background:var(--tag);
    border-radius:6px;border:2px solid var(--teal-bright);color:var(--teal-bright);
    font-size:14px;font-weight:700;letter-spacing:.6px;text-align:center;text-transform:uppercase}
  .testimonials{position:absolute;top:678px;left:0;right:0;bottom:0;
    background:linear-gradient(180deg,#3d4043 0%,var(--ink-mid) 20%,var(--ink-dark) 100%)}
  .testimonials__tab{position:absolute;top:-22px;left:18px;padding:8px 26px 8px 18px;background:var(--teal);
    color:var(--white);font-weight:900;font-size:17px;border-radius:0 16px 0 0;border-top:2px solid var(--teal-bright)}
  .testimonials__list{position:absolute;top:24px;left:30px;right:30px;color:var(--white);font-size:9.3px;line-height:1.34}
  .quote{margin-bottom:6px}
  .quote__by{display:block;font-weight:900;margin-top:1px}
  .flyer__footline{position:absolute;left:0;right:0;bottom:0;height:7px;background:var(--teal-bright)}
</style>
</head>
<body>
  <main class="flyer">
    <div class="flyer__topline"></div>
    <div class="centre-photo" role="img" aria-label="Photo of the tutoring centre: wooden bookshelves full of books around a large wooden table with blue chairs"></div>

    <svg class="headline-band" viewBox="0 0 600 140" preserveAspectRatio="none" aria-hidden="true">
      <path d="M0 14 Q300 -8 600 10 L600 124 Q300 146 0 128 Z" fill="var(--teal-dark)"/>
      <path d="M0 22 Q300 2 600 18 L600 118 Q300 138 0 122 Z" fill="var(--teal-deep)"/>
    </svg>
    <h1 class="headline">I'm charging $45 for sessions of an hour and 15 minutes. 2 sessions per week will cost $80. I tutor Monday to Friday afternoons and evenings along with all day Saturdays. The assessment is free.</h1>

    <section class="about">
      <div class="about__text">
        <p>I tutor children from K-9 in English and Maths. I'm mainly aiming at parents whose children are struggling a little bit at school although I can help children who are doing well too.</p>
        <p>I am highly skilled at helping children who can't read, I have a comprehensive program, the Calder program, that specifically teaches children the skills they need to read fluently and successfully.</p>
        <p>Similarly I have had a lot of experience at helping children improve their Maths skills. I am well resourced with a wide range of hands on resources, paper resources and electronic resources.</p>
        <p>Children will get better NAPLAN results if I tutor them (NAPLAN is the national series of tests in Australia).</p>
      </div>
    </section>

    <figure class="tutor">
      <div class="tutor__photo" role="img" aria-label="Portrait photo of tutor Marisol Penhaw in front of a bookshelf"></div>
      <figcaption class="tutor__name">Marisol Penhaw</figcaption>
    </figure>

    <section class="testimonials">
      <h2 class="testimonials__tab">Testimonials:</h2>
      <div class="testimonials__list">
        <p class="quote">Our son has been tutored by Marisol now for the past 2 years - we have noticed a big improvement with his spelling and mathematics. This has also helped our son's confidence in his daily schooling and he now has started to enjoy school again. Thanks Marisol
          <span class="quote__by">Tomas and Elena Brightwater</span></p>
        <p class="quote">Our children love going to Marisol's!! Yes you read that right - they LOVE going to learn! Marisol has the ability to tap into each child's strengths and weaknesses and makes learning fun! Our children's grades have improved more so, our son just got awarded a distinction in a science competition! Thanks so much Marisol.
          <span class="quote__by">Noreen Ashdale</span></p>
      </div>
    </section>
    <div class="flyer__footline"></div>
  </main>
</body>
</html>
```